3 Politically Incorrect Greeting Cards

I would like to see some clean, colorful, and modern designs for 3 "politically incorrect" greeting cards aimed at young, single, successful women. I would like them to say:

Card 1: " Congratulations on not marrying the wrong person"
Card 2: " Congratulations on buying a house without a husband"
Card 3: " Thank you for not forgetting about me now that you have a boyfriend"

My initial thought was to have a white background with simple black writing, but I think a colorful background with a white text box in the middle might be more appropriate. I can't imagine the cards having any images/icons on them, but I'm open to suggestions if you think it would improve on the design. You guys are likely more creative than I am.

I've included a couple pics of looks I like - but like I said - I'm open to suggestions and what I like may not be appropriate for these cards. All the cards can have a similar esthetic or theme (maybe the same fonts but different colors or different color florals in each) or they can be completely different.

Target Market(s)

Young, single, successful women mid-20s to mid 40's.

Font styles to use
Serif
Sans Serif
Other font styles liked:
• Watercolour lettering maybe

Colors

Designer to choose colors to be used in the design.

Requirements
Must have
• Clean, colorful, bright, professional looking. The right tone for the message.
• I think the message is bold so the writing and colors have to be as well. I have included examples of ideas I like.
Nice to have
• Images, illustrations, icons, maybe patterns or some decorative details. Something to make the card more interesting than just the words (like the blue background with black letters one I made). I like a bright pattern with a white box in the center with the text.
Should not have
• Special effects, galaxy pictures, ugly images, bland colors.

```html
<!DOCTYPE html>
<html lang="en">
<head>
<meta charset="utf-8">
<title>Congratulations on Buying a House Without a Husband</title>
<link rel="stylesheet" href="https://fonts.googleapis.com/css2?family=Montserrat:wght@300;400&display=swap">
<style>
  :root {
    --aqua: #c3ebef;
    --aqua-deep: #b6e3e8;
    --ink: #111313;
    --ink-soft: #232726;
    --ring: rgba(40, 44, 44, 0.75);
    --paper-white: #ffffff;
    --emblem-tone: rgba(255, 255, 255, 0.14);
  }
  * { margin: 0; padding: 0; box-sizing: border-box; }
  html, body {
    width: 857px;
    height: 1200px;
    overflow: hidden;
    background: var(--aqua);
  }
  .card {
    position: relative;
    width: 857px;
    height: 1200px;
    overflow: hidden;
  }
  .card__pattern {
    position: absolute;
    inset: 0;
    background: linear-gradient(180deg, var(--aqua) 0%, var(--aqua-deep) 50%, var(--aqua) 100%);
  }
  .card__ring {
    position: absolute;
    left: 146px;
    top: 315px;
    width: 566px;
    height: 566px;
    border-radius: 50%;
    border: 7px solid var(--ring);
  }
  .card__seal {
    position: absolute;
    left: 167px;
    top: 336px;
    width: 524px;
    height: 524px;
    border-radius: 50%;
    background: linear-gradient(90deg, var(--ink) 0%, var(--ink-soft) 100%);
    display: flex;
    flex-direction: column;
    align-items: center;
  }
  .card__message {
    margin-top: 93px;
    font-family: 'Montserrat', sans-serif;
    font-weight: 400;
    font-size: 29.6px;
    line-height: 42.5px;
    letter-spacing: 0.2px;
    color: var(--paper-white);
    text-align: center;
    text-transform: uppercase;
  }
  .card__emblem {
    margin-top: 12px;
    width: 106px;
    height: 106px;
    border-radius: 50%;
    background: var(--emblem-tone);
  }
</style>
</head>
<body>
  <main class="card">
    <div class="card__pattern" role="img" aria-label="Fine black chevron zigzag stripes on a light aqua background"></div>
    <div class="card__ring"></div>
    <section class="card__seal">
      <h1 class="card__message">
        Congratulations<br>on<br>buying a house<br>without<br>a husband
      </h1>
      <div class="card__emblem" role="img" aria-label="Small white line icon of a crossed-out partner inside an open circle"></div>
    </section>
  </main>
</body>
</html>
```